Cover Art Design for a Notebook

We are going to give away some note books to our marketing department and want an elegant art design for the cover. There is a theme centered around ABCD of marketing that we want to leverage in the design. So these letters should be prominent in the design. The ABCD stand for Agility, Boost, Customer, Data.

If you could Cleverly incorporate these words into the letters with a good design that would be good.

But please make the ABCD the focus of the artwork. The words associated with them should be subtle, in the background, visible but not the focus.

We are looking for stylish. We want people to feel proud of the ELEGANT DESIGN when they take out this notebook for business.

Also worth mentioning- We are a biotechnology company so if you incorporate elements in that theme in, on, or around the ABCD letters, it could be a good idea. As long as it doesn’t kill the rest of the design.

I will upload our logo for Veltrane Orwick Biologics later (you can see it online) and this will need to go in one corner.

Notebook will be A5 format. Image on front cover only. Need ASAP.

(Do not make baby blocks as we don’t want something that looks like a kids book)

Target Market(s)

business people who feel proud to pull out this notebook

Industry/Entity Type

Biotechnology

Colors
ec1f27
ffffff
000000

Requirements
Must have
• ELEGANT ART DESIGN USING ABCD
Nice to have
• see brief above
Should not have
• baby blocks

```html
<!DOCTYPE html>
<html lang="en">
<head>
<meta charset="utf-8">
<title>ABCD of Marketing — Notebook Cover</title>
<link rel="stylesheet" href="https://fonts.googleapis.com/css2?family=Arimo:wght@700&display=swap">
<style>
  :root {
    --brand-red: #e11d26;
    --ink: #111111;
    --paper: #ffffff;
    --hex-soft: rgba(255,255,255,0.38);
    --hex-faint: rgba(255,255,255,0.22);
    --hex-shadow: rgba(255,255,255,0.14);
    --hex-blush: rgba(240,190,196,0.55);
  }
  html, body {
    margin: 0;
    padding: 0;
    overflow: hidden;
    background: var(--paper);
  }
  .cover {
    position: relative;
    width: 855px;
    height: 1200px;
    overflow: hidden;
    background:
      radial-gradient(ellipse 420px 300px at 880px 1120px, #e0103f 0%, rgba(224,16,63,0) 100%),
      radial-gradient(ellipse 300px 380px at 860px 760px, #1a1a1a 0%, rgba(26,26,26,0.7) 40%, rgba(26,26,26,0) 100%),
      radial-gradient(ellipse 520px 460px at 300px 620px, #e77f8a 0%, rgba(231,127,138,0.55) 45%, rgba(231,127,138,0) 100%),
      radial-gradient(ellipse 620px 520px at 520px 900px, #ee9aa3 0%, rgba(238,154,163,0) 100%),
      linear-gradient(180deg, #ffffff 0%, #ffffff 14%, #f6dfe1 30%, #efb9bf 60%, #f2d4d7 100%);
    font-family: "Arimo", Arial, sans-serif;
  }
  .dna-artwork {
    position: absolute;
    left: 400px;
    top: 300px;
    width: 455px;
    height: 560px;
    background: radial-gradient(ellipse at 60% 50%, rgba(140,40,55,0.45) 0%, rgba(90,40,45,0.25) 45%, rgba(90,40,45,0) 75%);
  }
  .molecule-artwork {
    position: absolute;
    left: 0;
    top: 680px;
    width: 330px;
    height: 520px;
    background: radial-gradient(ellipse at 35% 50%, rgba(150,140,142,0.45) 0%, rgba(190,180,182,0.25) 50%, rgba(220,210,212,0) 80%);
  }
  .brand {
    position: absolute;
    top: 62px;
    right: 57px;
    display: flex;
    align-items: center;
    gap: 14px;
    color: var(--brand-red);
    font-weight: 700;
    font-size: 36px;
    line-height: 1;
    white-space: nowrap;
  }
  .brand-mark {
    width: 22px;
    height: 22px;
    background: var(--brand-red);
  }
  .hex-field {
    position: absolute;
    inset: 0;
  }
  .hex { fill: var(--hex-soft); }
  .hex--faint { fill: var(--hex-faint); }
  .hex--shadow { fill: var(--hex-shadow); }
  .hex--blush { fill: var(--hex-blush); }
  .letter {
    fill: var(--brand-red);
    font-family: "Arimo", Arial, sans-serif;
    font-weight: 700;
    font-size: 160px;
    text-anchor: middle;
    dominant-baseline: central;
  }
</style>
</head>
<body>
<main class="cover">
  <div class="dna-artwork" role="img" aria-label="Soft-focus red DNA double helix rising diagonally behind the letters"></div>
  <div class="molecule-artwork" role="img" aria-label="Grey ball-and-stick molecule models in soft focus"></div>

  <header class="brand">
    <span class="brand-mark"></span>
    <span class="brand-name">Veltrane Orwick Biologics</span>
  </header>

  <svg class="hex-field" width="855" height="1200" viewBox="0 0 855 1200" aria-label="ABCD of marketing">
    <polygon class="hex hex--blush" points="202,145 257,177 257,241 202,273 147,241 147,177"/>
    <polygon class="hex" points="260,267 418,358 418,540 260,631 102,540 102,358"/>
    <polygon class="hex hex--faint" points="205,609 264,643 264,711 205,745 146,711 146,643"/>
    <polygon class="hex hex--shadow" points="630,658 687,691 687,757 630,790 573,757 573,691"/>
    <polygon class="hex" points="417,498 552,576 552,732 417,810 282,732 282,576"/>
    <polygon class="hex" points="394,706 540,790 540,958 394,1042 248,958 248,790"/>
    <polygon class="hex" points="638,842 782,925 782,1091 638,1174 494,1091 494,925"/>
    <polygon class="hex hex--faint" points="822,936 857,956 857,996 822,1016 787,996 787,956"/>

    <text class="letter" x="252" y="446">A</text>
    <text class="letter" x="417" y="656">B</text>
    <text class="letter" x="380" y="876">C</text>
    <text class="letter" x="632" y="1030">D</text>
  </svg>
</main>
</body>
</html>
```